Website Home Page for Women's Health Medical Office

Redesign existing homepage for website using existing logo. Current website location is www.lumawomenscare.com. Please give it a modern, streamlined, playful feel.

Please give it a feminine feel and make it bright and cheerful using logo colors.

Target Market(s)

Women between the ages of 25-45

Industry/Entity Type

Medical Office

Coding

Coded - Design and coding required

Number of Pages Required

1 page

Font styles to use
Sans Serif
Other font styles liked:
• SEGOI UI script for text and GIL SANS for bold (or their equivilent)

Colors
E54698
E96AAD
F1A4CE
F9D9EA
FCEFF6

Requirements
Must have
• Existing logo. Logo Colors. Feminine, cheerful, simple design. all relevant contact information
Nice to have
• clean lines and streamlined look
Should not have
• Cluttered

```html
<!DOCTYPE html>
<html lang="en">
<head>
<meta charset="utf-8">
<title>Luma Women's Care – Home</title>
<link rel="stylesheet" href="https://fonts.googleapis.com/css2?family=Montserrat:ital,wght@0,400;0,500;0,600;0,700;0,800;1,400;1,500&family=Open+Sans:wght@400;600&display=swap">
<style>
:root{
  --pink:#fd0a7e;
  --pink-soft:#f98dbd;
  --pink-band:#fb7fb4;
  --ink:#2d2d2d;
  --text:#444;
  --dark-bar:#333333;
  --panel:#f3f3f3;
  --footer:#e9e9e9;
  --white:#ffffff;
}
*{box-sizing:border-box;margin:0;padding:0}
html,body{width:1200px;height:3103px;overflow:hidden}
body{position:relative;background:var(--white);font-family:'Open Sans',sans-serif;color:var(--text)}
.abs{position:absolute}

.top-bar{left:0;top:0;width:1200px;height:25px;background:var(--dark-bar);color:#fff;font-size:10px;font-weight:600}
.top-bar .address{left:107px;top:6px;display:flex;align-items:center;gap:5px}
.top-bar .contacts{right:63px;top:6px;display:flex;align-items:center;gap:5px}
.top-bar svg{width:9px;height:9px;fill:var(--pink)}

.nav-bar{left:0;top:25px;width:1200px;height:77px;background:var(--pink)}
.nav-links{right:60px;top:53px;display:flex;gap:23px;color:#fff;font-family:'Open Sans',sans-serif;font-size:13px;font-weight:600}

.brand-box{left:94px;top:25px;width:243px;height:201px;background:#fff;box-shadow:0 2px 8px rgba(0,0,0,.18);display:flex;flex-direction:column;align-items:center;justify-content:center;gap:12px}
.brand-mark{width:54px;height:54px;border-radius:50%;background:var(--pink)}
.brand-name{font-family:'Montserrat',sans-serif;font-weight:700;font-size:21px;color:var(--ink);text-align:center;line-height:1.15;white-space:nowrap}

.hero{left:0;top:102px;width:1200px;height:561px;background:linear-gradient(90deg,#ffffff 0%,#f7f7f5 35%,#efeeea 60%,#e9e3dc 100%)}
.hero-photo{left:410px;top:102px;width:790px;height:561px;background:linear-gradient(100deg,rgba(240,238,234,0) 0%,#ede6df 30%,#d8bfae 60%,#b88c74 85%,#8e6250 100%)}
.hero-title{left:104px;top:333px;font-family:'Montserrat',sans-serif;font-weight:500;font-size:38px;line-height:43px;color:var(--ink)}
.btn{background:var(--pink);color:#fff;font-family:'Montserrat',sans-serif;font-weight:500;border-radius:5px;display:flex;align-items:center;justify-content:center}
.hero-btn{left:105px;top:483px;width:259px;height:53px;font-size:23px}

.welcome{left:5px;top:663px;width:1195px;height:584px;background:var(--panel)}
.doctor-photo{left:113px;top:786px;width:348px;height:336px;background:radial-gradient(ellipse at 50% 60%,#8a7a74 0%,#4d5466 45%,#2f3545 100%)}
.welcome-title{left:488px;top:771px;font-family:'Montserrat',sans-serif;font-weight:500;font-size:37px;line-height:44px;color:var(--ink);white-space:nowrap}
.welcome-title .accent{color:var(--pink);font-size:31px;letter-spacing:-.3px;display:block}
.welcome-copy{left:489px;top:885px;width:584px;font-size:10.6px;line-height:18px;color:#333;text-align:justify}
.welcome-copy p+p{margin-top:18px}
.about-btn{left:488px;top:1068px;width:206px;height:52px;font-size:23px}

.patients-band{left:0;top:1247px;width:1200px;height:822px;background:linear-gradient(180deg,#fb86b8 0%,#fb6fa9 55%,#fb5d9e 100%)}
.band-kicker{left:0;top:1322px;width:1200px;text-align:center;font-family:'Montserrat',sans-serif;font-style:italic;font-weight:400;font-size:38px;color:#fff}
.band-title{left:0;top:1368px;width:1200px;text-align:center;font-family:'Montserrat',sans-serif;font-weight:800;font-size:52px;color:#fff;letter-spacing:.5px}
.band-btn{left:458px;top:1440px;width:283px;height:57px;background:linear-gradient(180deg,#fff 0%,#ececec 100%);color:var(--pink);font-size:24px;border-radius:4px;box-shadow:0 1px 3px rgba(0,0,0,.15)}
.band-photo{left:0;top:1540px;width:1200px;height:529px;background:radial-gradient(ellipse at 60% 55%,#ff6aa8 0%,#fc5c9f 40%,rgba(251,93,158,0) 75%)}

.services-kicker{left:0;top:2175px;width:1200px;text-align:center;font-family:'Montserrat',sans-serif;font-size:19px;color:var(--pink)}
.services-title{left:0;top:2200px;width:1200px;text-align:center;font-family:'Montserrat',sans-serif;font-weight:500;font-size:37px;color:var(--ink)}
.service{width:227px}
.service-photo{width:227px;height:157px}
.service h3{margin-top:34px;font-family:'Montserrat',sans-serif;font-weight:500;font-size:19px;color:var(--ink)}
.service p{margin-top:8px;font-size:10.6px;line-height:18px;color:#444;text-align:justify}
.more-btn{position:absolute;top:358px;left:0;width:44px;height:23px;background:var(--pink);color:#fff;font-size:10px;font-weight:600;border-radius:3px;display:flex;align-items:center;justify-content:center}

.site-footer{left:0;top:2809px;width:1200px;height:255px;background:var(--footer)}
.footer-brand{left:126px;top:2838px;width:215px;height:168px;display:flex;flex-direction:column;align-items:center;justify-content:center;gap:12px}
.footer-brand .brand-name{font-size:19px}
.footer-col h4{font-family:'Montserrat',sans-serif;font-weight:600;font-size:16px;color:var(--pink);margin-bottom:14px}
.footer-col{font-size:12.5px;color:#555;line-height:16px}
.quick-links{list-style:none}
.quick-links li{display:flex;align-items:center;gap:12px;font-size:14px;line-height:22.5px}
.quick-links svg{width:7px;height:8px;fill:var(--pink)}
.areas a{display:block;width:146px;border-bottom:1px solid var(--pink);font-size:13px;color:#555;text-decoration:none;padding-bottom:3px;margin-bottom:5px}
.bottom-bar{left:0;top:3064px;width:1200px;height:39px;background:var(--dark-bar);color:#ddd;font-size:12px;display:flex;align-items:center;justify-content:center}
</style>
</head>
<body>

<div class="abs top-bar">
  <div class="abs address"><svg viewBox="0 0 10 10"><path d="M5 0a3.5 3.5 0 0 0-3.5 3.5C1.5 6 5 10 5 10s3.5-4 3.5-6.5A3.5 3.5 0 0 0 5 0zm0 5a1.5 1.5 0 1 1 0-3 1.5 1.5 0 0 1 0 3z"/></svg>1840 Willow Crest Avenue, Suite 210, Fairhaven, CA 90215</div>
  <div class="abs contacts">
    <svg viewBox="0 0 10 10"><path d="M2 0l2 2.5-1 1.2a6 6 0 0 0 3.3 3.3l1.2-1L10 8l-1.5 2C4 10 0 6 0 1.5z"/></svg>(555) 014-2280
    <svg viewBox="0 0 10 10"><path d="M0 2h10v6H0zM0 2l5 3.5L10 2" stroke="#333" stroke-width=".8"/></svg>admin@lumawomenscare.com
    <svg viewBox="0 0 10 10"><rect x="2.5" y="0" width="5" height="10" rx="1"/></svg>555-014-2291
  </div>
</div>

<div class="abs nav-bar"></div>
<nav class="abs nav-links"><span>Home</span><span>Services</span><span>Resources</span><span>About us</span><span>Contact us</span></nav>

<section class="abs hero"></section>
<div class="abs hero-photo" role="img" aria-label="Smiling mother holding her newborn baby close"></div>
<div class="abs brand-box"><span class="brand-mark"></span><span class="brand-name">Luma Women's Care</span></div>
<h1 class="abs hero-title">Welcoming to<br>Serving Willow Springs<br>medical center</h1>
<a class="abs btn hero-btn">Make appointment</a>

<section class="abs welcome"></section>
<div class="abs doctor-photo" role="img" aria-label="Portrait of the practice physician in navy scrubs"></div>
<h2 class="abs welcome-title">Welcome to<span class="accent">LUMA WOMEN'S CARE, FAIRHAVEN, CA</span></h2>
<div class="abs welcome-copy">
  <p>At Luma Women's Care in Fairhaven, California, we believe better health starts when the patient is educated. For this reason, we take time to listen to our patients concerns, explain each option available, and to answer any questions our patients may have so that they can make informed decisions. At Luma Women's Care, our providers tailor every procedure performed and treatment option recommended to meet the specific needs of our patients. We remain up-to-date on the latest technology and practice guidelines for women's health.</p>
  <p>Our medical providers will take time to give you the personalized health care you deserve. This includes taking time to listen to you and screening you for problems to help ensure that any health issues are diagnosed and treated as early as possible.</p>
</div>
<a class="abs btn about-btn">More about us</a>

<section class="abs patients-band"></section>
<div class="abs band-photo" role="img" aria-label="Happy baby lying on its smiling mother, pink tinted"></div>
<p class="abs band-kicker">Better Health Starts Here!</p>
<h2 class="abs band-title">NOW ACCEPTING NEW PATIENTS</h2>
<a class="abs btn band-btn">Make appointment</a>

<p class="abs services-kicker">Health Services Offered</p>
<h2 class="abs services-title">HOW CAN WE HELP YOU?</h2>

<article class="abs service" style="left:125px;top:2288px">
  <div class="service-photo" role="img" aria-label="Pregnant woman consulting with a nurse" style="background:linear-gradient(120deg,#3fb0b0 0%,#e8e8e6 40%,#f4f2ef 100%)"></div>
  <h3>Pregnancy care</h3>
  <p>Receiving regular care in pregnancy is important for the health of both you and your baby. Our obstetrcians work with you every step of the way during your pregnancy and delivery to make sure your individual needs are met and co ensure this special journey is a memorable one.</p>
  <a class="more-btn">More</a>
</article>
<article class="abs service" style="left:372px;top:2288px">
  <div class="service-photo" role="img" aria-label="Hand holding a birth control pill pack" style="background:linear-gradient(120deg,#eef0ee 0%,#dcdedd 50%,#e9c7cc 100%)"></div>
  <h3>Birth Control</h3>
  <p>Receiving regular care in pregnancy is important for the health of both you and your baby. Our obstetrcians work with you every step of the way during your pregnancy and delivery to make sure your individual needs are met and co ensure this special journey is a memorable one.</p>
  <a class="more-btn">More</a>
</article>
<article class="abs service" style="left:618px;top:2288px">
  <div class="service-photo" role="img" aria-label="Woman receiving an ultrasound exam" style="background:linear-gradient(120deg,#e9eaeb 0%,#f5f4f3 50%,#d8d9db 100%)"></div>
  <h3>Wel Women Exams</h3>
  <p>Receiving regular care in pregnancy is important for the health of both you and your baby. Our obstetrcians work with you every step of the way during your pregnancy and delivery to make sure your individual needs are met and co ensure this special journey is a memorable one.</p>
  <a class="more-btn">More</a>
</article>
<article class="abs service" style="left:868px;top:2288px">
  <div class="service-photo" role="img" aria-label="Doctor with clipboard speaking with a patient" style="background:linear-gradient(120deg,#6e6a68 0%,#cfcfcf 40%,#ececec 100%)"></div>
  <h3>WOMEN'S HEALTH</h3>
  <p>Whether you are dealing with painful or irregular periods, fibroids, or other women's health issues, we can help. We offer a variety of the most up-to-date treatment options to help you regain your lifestyle.</p>
  <a class="more-btn">More</a>
</article>

<footer class="abs site-footer"></footer>
<div class="abs footer-brand"><span class="brand-mark"></span><span class="brand-name">Luma Women's Care</span></div>
<div class="abs footer-col" style="left:418px;top:2854px">
  <h4>Contact info</h4>
  <p>1840 Willow Crest Avenue,<br>Suite 210, Fairhaven, CA 90215</p>
  <p style="margin-top:8px">(555) 014-2280<br>admin@lumawomenscare.com<br>555-014-2291</p>
</div>
<div class="abs footer-col" style="left:693px;top:2854px">
  <h4>Quick Link</h4>
  <ul class="quick-links">
    <li><svg viewBox="0 0 7 8"><path d="M0 0l7 4-7 4z"/></svg>Home</li>
    <li><svg viewBox="0 0 7 8"><path d="M0 0l7 4-7 4z"/></svg>Services</li>
    <li><svg viewBox="0 0 7 8"><path d="M0 0l7 4-7 4z"/></svg>Resources</li>
    <li><svg viewBox="0 0 7 8"><path d="M0 0l7 4-7 4z"/></svg>About us</li>
    <li><svg viewBox="0 0 7 8"><path d="M0 0l7 4-7 4z"/></svg>Contact us</li>
  </ul>
</div>
<div class="abs footer-col areas" style="left:914px;top:2854px">
  <h4>Practice Areas</h4>
  <a>PREGNANCY CARE</a>
  <a>BIRTH CONTROL</a>
  <a>WELL WOMAN EXAMS</a>
  <a>WOMEN'S HEALTH</a>
</div>
<div class="abs bottom-bar">Copyright 2020, Northlane Studio, All Right Reserved</div>

</body>
</html>
```